International oil and gas consultancy needs a business card design

We need a business card design for a new oil and gas consultancy business based in Perth Australia. This is a professional services business and needs a moderately conservative type of business card. The business card also needs to be simple and uncluttered. The colour of the business logo is dark red (see attached file).
The front of the card should have a white background and mainly black lettering and perhaps some use of dark red and/or grey (your choice).
The back of the card should have a light grey background with dark red, black and or both dark red & black lettering (your choice).
Please find attached a clear brief of how I would like the business card designed.

Hello Everyone, I have slightly modified the brief. The main change is to incorporate some dark red and grey colours into the card, while still keeping the black lettering dominant. I have made the changes in the attached detailed brief document. Regards

Please note, the front of the card must say Pelwick Review Services (in addition to the logo).

Conservative

• brief has been updated. please refer to attachment for details.

Front of the card MUST say Pelwick Review Services (in addition to the logo)

```html
<!DOCTYPE html>
<html lang="en">
<head>
<meta charset="utf-8">
<title>Pelwick Review Services – Business Card</title>
<link href="https://fonts.googleapis.com/css2?family=Arimo:ital,wght@0,400;0,700;1,400&display=swap" rel="stylesheet">
<style>
  :root {
    --page-bg: #d9d9d9;
    --card-white: #ffffff;
    --card-grey: #e6e6e6;
    --band-grey: #5c5c5c;
    --brand-red: #8e1b1b;
    --ink: #111111;
    --ink-soft: #4a4a4a;
  }
  * { margin: 0; padding: 0; box-sizing: border-box; }
  html, body { width: 900px; height: 1200px; overflow: hidden; }
  body {
    background: var(--page-bg);
    font-family: "Arimo", Arial, sans-serif;
    color: var(--ink);
    position: relative;
  }
  .card-pair {
    position: absolute;
    top: 482px;
    left: 35px;
    display: flex;
    gap: 30px;
  }
  .card {
    position: relative;
    width: 400px;
    height: 236px;
    background: var(--card-grey);
    box-shadow: 0 2px 8px rgba(0,0,0,0.25);
    overflow: hidden;
  }
  .card-header {
    height: 78px;
    background: var(--card-white);
    position: relative;
  }
  .brand-name {
    position: absolute;
    left: 13px;
    top: 14px;
    font-size: 50px;
    font-weight: 700;
    letter-spacing: 1px;
    color: var(--brand-red);
    line-height: 1;
  }
  .company-band {
    height: 14px;
    background: var(--band-grey);
    color: var(--card-white);
    font-size: 11.5px;
    line-height: 14px;
    padding-left: 13px;
    text-transform: uppercase;
  }
  .card-body { position: relative; height: 144px; }

  /* Front */
  .person { position: absolute; right: 14px; top: 7px; text-align: right; }
  .person-name { font-size: 18px; font-weight: 700; }
  .person-title { font-size: 15px; color: var(--ink-soft); margin-top: 2px; }
  .person-region { font-size: 12.5px; color: var(--ink-soft); margin-top: 3px; }
  .contact {
    position: absolute; right: 14px; bottom: 12px;
    text-align: right; font-size: 13px; line-height: 15px;
  }
  .abn { position: absolute; left: 13px; bottom: 10px; font-size: 13px; }

  /* Back */
  .tagline {
    position: absolute; left: 20px; top: 46px; width: 200px;
    font-style: italic; font-size: 12.5px; line-height: 16px;
  }
  .services {
    position: absolute; left: 243px; top: 6px;
    list-style: none; font-size: 14.5px; line-height: 17px; color: #333;
  }
  .services li::before {
    content: ""; display: inline-block;
    width: 8px; height: 8px; border-radius: 50%;
    background: #333; margin-right: 4px; vertical-align: 1px;
  }
</style>
</head>
<body>
  <main class="card-pair">
    <section class="card card-front" aria-label="Card front">
      <header class="card-header"><span class="brand-name">PRS</span></header>
      <div class="company-band">Pelwick Review Services</div>
      <div class="card-body">
        <div class="person">
          <p class="person-name">Adam Renwick</p>
          <p class="person-title">Director</p>
          <p class="person-region">Australasia and South East Asia</p>
        </div>
        <p class="abn">ABN: 51 824 307 926</p>
        <div class="contact">
          <p>+61 (0)400 118 392</p>
          <p>adam@pelwickreview.com</p>
          <p>www.pelwickreview.com</p>
        </div>
      </div>
    </section>

    <section class="card card-back" aria-label="Card back">
      <header class="card-header"><span class="brand-name">PRS</span></header>
      <div class="company-band">Pelwick Review Services</div>
      <div class="card-body">
        <p class="tagline">Specialist Financial Consultants to the Oil and Gas Industry</p>
        <ul class="services">
          <li>Joint Venture Audits</li>
          <li>Contract Audits</li>
          <li>Operational Audits</li>
        </ul>
      </div>
    </section>
  </main>
</body>
</html>
```